Mining Engineering Services

I would like a 1 page flyer promoting RVT Mining Pty Ltd engineering services using a UAV (Unmanned aerial vehicle). I want something simple yet captures the readers attention. I have a promo video that I would like to attach a hyper link to this brochure. I have four other brochures to make after the successful completion of this one.

Target Market(s)

Mining Industry

Requirements
Must have
• Details from the word doc attached.
• Contact detail to be included;
• Dean Whitlock
• Email - dean.whitlock@rvtmining-example.com
• Phone - 0418552913

```html
<!DOCTYPE html>
<html lang="en">
<head>
<meta charset="utf-8">
<title>RVT Mining Pty Ltd – Engineering Services Flyer</title>
<link rel="stylesheet" href="https://fonts.googleapis.com/css2?family=Oswald:wght@400;500&family=Open+Sans:ital,wght@0,400;0,600;0,700;1,400&display=swap">
<style>
  :root {
    --navy: #0d2a7a;
    --navy-deep: #081d5c;
    --royal: #1a46b8;
    --cyan: #2fa8ff;
    --ink: #1b1b2b;
    --muted: #b9c8ec;
    --paper: #ffffff;
    --backdrop: #d9d9db;
  }
  * { box-sizing: border-box; margin: 0; padding: 0; }
  html, body { width: 1200px; height: 687px; overflow: hidden; }
  body { background: var(--backdrop); font-family: "Open Sans", sans-serif; position: relative; }

  .flyer {
    position: absolute; left: 370px; top: 18px; width: 460px; height: 650px;
    background: var(--paper); overflow: hidden;
    box-shadow: 0 6px 18px rgba(0,0,0,.18);
  }

  /* left navy column */
  .sidebar {
    position: absolute; left: 0; top: 0; width: 166px; height: 100%;
    background: linear-gradient(180deg, var(--navy) 0%, var(--navy-deep) 100%);
    color: var(--muted);
  }
  .brand { position: absolute; top: 44px; left: 0; width: 100%; text-align: center; }
  .brand-dot { display: block; width: 36px; height: 36px; margin: 0 auto 6px; border-radius: 50%; background: var(--royal); border: 2px solid #dfe7ff; }
  .brand-name { font-weight: 600; color: #fff; font-size: 10px; letter-spacing: 3px; }

  .bio-tag {
    position: absolute; top: 114px; left: 30px; width: 100px; height: 38px;
    border: 1px solid #fff; border-left-color: transparent; border-right-color: transparent;
    color: #fff; text-align: center; font-weight: 600; font-size: 11.5px; line-height: 16px; padding-top: 3px;
  }
  .bio-tag::before, .bio-tag::after { content: ""; position: absolute; top: -1px; width: 1px; height: 38px; background: #fff; }
  .bio-tag::before { left: 0; } .bio-tag::after { right: 0; }

  .bio {
    position: absolute; top: 188px; left: 12px; width: 145px;
    font-size: 7.6px; line-height: 12.3px; text-align: justify; color: var(--muted);
  }

  .video { position: absolute; left: 21px; width: 122px; border: 2px solid #c9d3ea; }
  .video-a { top: 390px; height: 74px; background: linear-gradient(180deg, #9c8a6a 0%, #c9a86a 45%, #b79257 100%); }
  .video-b { top: 468px; height: 60px; background: linear-gradient(135deg, #2b2b2e 0%, #4a4a50 60%, #1e1e22 100%); }
  .play { position: absolute; left: 50%; top: 50%; width: 14px; height: 10px; margin: -5px 0 0 -7px; background: #e53b2c; border-radius: 3px; }
  .play::after { content: ""; position: absolute; left: 5px; top: 2.5px; border-left: 5px solid #fff; border-top: 2.5px solid transparent; border-bottom: 2.5px solid transparent; }
  .video-link { position: absolute; top: 532px; left: 0; width: 100%; text-align: center; font-size: 7px; color: var(--muted); text-decoration: underline; }

  .contact { position: absolute; top: 552px; left: 0; width: 100%; text-align: center; }
  .contact-icons { display: flex; justify-content: center; gap: 16px; margin-bottom: 3px; }
  .contact-name { color: #fff; font-size: 10px; letter-spacing: 3px; margin-bottom: 4px; }
  .contact-line { font-size: 7.3px; color: var(--muted); line-height: 13px; }

  .sidebar-rule { position: absolute; left: 0; top: 640px; width: 166px; height: 2px; background: var(--cyan); }

  /* header photo band */
  .hero {
    position: absolute; left: 166px; top: 0; width: 294px; height: 218px;
    background: linear-gradient(180deg, #2456b3 0%, #6d8fbf 28%, #8a6a48 45%, #5a4a3c 70%, #2a2523 100%);
  }
  .hero-title { position: absolute; left: 182px; top: 138px; font-family: "Oswald", sans-serif; font-weight: 400; line-height: 1; white-space: nowrap; }
  .hero-title .company { display: block; color: #fff; font-size: 31px; letter-spacing: -.6px; }
  .hero-title .service { display: block; color: var(--cyan); font-size: 27px; margin-top: 3px; letter-spacing: -.6px; }

  /* content */
  .block { position: absolute; left: 186px; width: 260px; }
  .marker { position: absolute; left: 158px; width: 16px; height: 26px; border-radius: 0 13px 13px 0; background: var(--royal); }
  .block h2 { font-size: 10.2px; font-weight: 700; color: var(--royal); line-height: 12.5px; margin-bottom: 6px; }
  .block ul { list-style: none; font-style: italic; font-size: 7.3px; line-height: 10.1px; color: var(--ink); }
  .services li::before { content: "•"; }
  .bulleted { padding-left: 6px; }
  .bulleted li::before { content: "• "; margin-left: -6px; }

  .services { top: 236px; }
  .uav { top: 402px; }
  .sensors { top: 560px; }

  .footer-url { position: absolute; left: 186px; top: 624px; font-size: 6.8px; font-weight: 700; font-style: italic; color: var(--navy); line-height: 10px; }
  .footer-rule { position: absolute; left: 166px; top: 640px; width: 260px; height: 1px; background: var(--cyan); }
  .footer-dot { position: absolute; left: 420px; top: 620px; width: 20px; height: 20px; border-radius: 50%; background: var(--royal); }
</style>
</head>
<body>
<main class="flyer">
  <aside class="sidebar">
    <div class="brand"><span class="brand-dot"></span><span class="brand-name">RVT MINING</span></div>
    <div class="bio-tag">COMPANY<br>SHORT BIO</div>
    <p class="bio">RVT Mining Pty Ltd is a Mining Engineering consultancy company with over 15 year's experience in the Mining industry. RVT Mining Pty Ltd provides value adding mining engineering services with the utilisation of industry leading UAV (Unmanned Aerial Vehicle) technology. RVT Mining utilises multiple sensors in the UAV to provide custom solutions to your Mine site. Unlike other UAV survey providers, RVT Mining's engineering expertise can provide assistance from concept to reconciliation of your project.</p>

    <a class="video video-a" role="img" aria-label="Promo video thumbnail: aerial view over a sandy mine site"><span class="play"></span></a>
    <div class="video video-b" role="img" aria-label="Thermal imaging still of a stockpile"></div>
    <span class="video-link">www.rvt-video-example.com</span>

    <div class="contact">
      <div class="contact-icons">
        <svg width="9" height="7" viewBox="0 0 9 7" aria-hidden="true"><rect x=".5" y=".5" width="8" height="6" fill="none" stroke="#fff"/><path d="M.5 .5 4.5 4 8.5 .5" fill="none" stroke="#fff"/></svg>
        <svg width="8" height="8" viewBox="0 0 8 8" aria-hidden="true"><path d="M1.5 .5c.8 0 1.2 1.6 1 2.2-.3.4-.8.5-.5 1.1.5.9 1.2 1.6 2.1 2 .6.3.7-.2 1.1-.5.6-.2 2.2.2 2.2 1 0 .9-1.2 1.3-2 1.1C2.8 6.7 1.3 5.2.6 2.6.3 1.7.6.5 1.5.5z" fill="#fff"/></svg>
      </div>
      <div class="contact-name">DEAN WHITLOCK</div>
      <div class="contact-line">dean.whitlock@rvtmining-example.com</div>
      <div class="contact-line">041 855 2913</div>
    </div>
    <div class="sidebar-rule"></div>
  </aside>

  <section class="hero" role="img" aria-label="Open-pit mine terraces at sunset with a UAV flying overhead"></section>
  <h1 class="hero-title"><span class="company">RVT MINING PTY LTD</span><span class="service">ENGINEERING SERVICES</span></h1>

  <span class="marker" style="top:230px"></span>
  <section class="block services">
    <h2>Services include but are not limited to</h2>
    <ul>
      <li>Mine operation design and scheduling</li>
      <li>Pit optimisation</li>
      <li>Rehabilitation design and planning</li>
      <li>Surface water drainage</li>
      <li>Open pit/stockpile volumes</li>
      <li>DEM (Digital Elevation Models)</li>
      <li>Reconciliationreporting</li>
      <li>Thermal imaging for volatile materials</li>
      <li>Pit wall inspections</li>
      <li>Geo referenced Ortho-mosaics</li>
      <li>Site rehabilitation inspections</li>
      <li>Multispectral imaging</li>
      <li>Surveying services</li>
    </ul>
  </section>

  <span class="marker" style="top:400px"></span>
  <section class="block uav">
    <h2>UAV (Unmanned Aerial Vehicle) information<br>SkyTrace S200 UAV System</h2>
    <ul class="bulleted">
      <li>1.8m wing span</li>
      <li>Fully transportable</li>
      <li>Operates under fully autonomous or manualcontrol</li>
      <li>Highly accurate navigation and positioningsystems</li>
      <li>Versatile and flexible operations</li>
      <li>Long flight time + 45min (large surveys per flight)</li>
      <li>Able to operate low rain</li>
      <li>Able to operate in high wind</li>
      <li>Parachute recovery</li>
      <li>Assisted Launch</li>
      <li>Multiple Pod &amp; Sensor Capable</li>
    </ul>
  </section>

  <span class="marker" style="top:556px"></span>
  <section class="block sensors">
    <h2>Sensors utilised</h2>
    <ul class="bulleted">
      <li>RGB 24 mega pixel camera (Digital Elevation Models)</li>
      <li>Infra-red camera (Thermal imaging)</li>
      <li>NDVI (Multispectral imaging)</li>
      <li>Magnetometer (Magnetic surveys)</li>
    </ul>
  </section>

  <span class="footer-url">www.rvtmining-example.com</span>
  <div class="footer-rule"></div>
  <span class="footer-dot"></span>
</main>
</body>
</html>
```